Premium Skincare Packaging Design for Vale Hollow

Vale Hollow (https://valehollowgoods.com) is a premium wellness brand from Canada specializing in beef tallow (for cooking) and now expanding into natural skincare. We are seeking packaging design concepts for two new 60 ml skincare products made with grass-fed beef tallow.
Our goal is to achieve a clean, minimalist yet luxurious look that reflects purity, quality and sophistication. The design should look premium enough for high-end skincare shelves while maintaining a natural, grounded feel.
You will be designing:
- Jar label (wrap-around design) for a 60 ml glass jar with black lid
- Round lid sticker (for the top of the black lid)
- Square outer box (for each jar)
- Both products are very similar, so the differentiation can be minimal.

Products to Design
1. Everyday Suet Salve
Jar: Frosted glass, 60 ml with black lid
Purpose: Moisturizer for face, lips, hands, and body
Ingredients: Grass-fed beef tallow, beeswax, honey, vitamin E
Tone: Natural, pure, versatile, gentle
Tagline: “Crafted from nature’s simplest elements”
Preferred color palette:
Light / off-white background
Beige and honey accents
Black or dark brown typography
Mood: Minimalist apothecary meets warm, natural simplicity
2. Visage Suet Lotion
Purpose: Face moisturizer with nourishing tallow and botanicals
Tone: Refined, elegant, modern, premium
Tagline: “The strength of tallow, refined for your face”
Preferred color palette:
Deep charcoal or black background
Gold or cream typography
Accent in subtle metallic tones (gold or bronze)
Mood: Modern luxury with understated confidence
Design Deliverables
For each product, submit:
1) Jar Label (Wrap-around)
- Include product name, logo, tagline, ingredients, and size (60 ml / 2 fl oz).
- Space for barcode and manufacturing details (leave placeholder).
2) Round Lid Sticker
- Centered logo and minimalist border or accent ring.
3) Outer Paper Box (Square)
- Matching color palette and typography.
- Clean layout featuring the Vale Hollow logo and tagline.
- Text to include: product name, tagline, ingredients and size.

Brand Guidelines
Logo: Use the existing Vale Hollow logo (we’ll upload it for reference).
Typography: Clean and elegant — sans-serif or classic serif fonts.
Tone: Pure, premium, and intentional — less is more.
Design cohesion: Both products must look like part of one collection.

```html
<!DOCTYPE html>
<html lang="en">
<head>
<meta charset="utf-8">
<title>Vale Hollow — Skincare Packaging</title>
<link rel="stylesheet" href="https://fonts.googleapis.com/css2?family=Archivo:wdth,wght@125,800&family=Figtree:wght@400;500&display=swap">
<style>
  :root {
    --backdrop: #bcb9b7;
    --cream: #e2d8ca;
    --ink: #000000;
    --display: "Archivo", "Arial Black", sans-serif;
    --text: "Figtree", "Helvetica Neue", Arial, sans-serif;
  }
  * { margin: 0; padding: 0; box-sizing: border-box; }
  html, body { width: 1200px; height: 1200px; overflow: hidden; }
  body { background: var(--backdrop); position: relative; font-family: var(--text); }

  .jar-label { position: absolute; left: 83px; top: 199px; width: 762px; height: 360px; background: var(--cream); }
  .jar-label__tab { position: absolute; left: 217px; top: 0; width: 328px; height: 186px; background: var(--ink); border-radius: 0 0 20px 20px; }
  .jar-label__brand-tab { position: absolute; left: 109px; top: 0; width: 114px; height: 60px; background: var(--cream); border-radius: 0 0 8px 8px; display: flex; align-items: center; justify-content: center; }
  .jar-label__size { position: absolute; left: 314px; bottom: 0; width: 132px; height: 29px; background: var(--ink); color: var(--cream); border-radius: 8px 8px 0 0; font-size: 11px; display: flex; align-items: center; justify-content: center; }

  .wordmark { font-family: var(--text); font-weight: 500; text-transform: uppercase; letter-spacing: 0.12em; font-size: 11px; line-height: 1; white-space: nowrap; }
  .wordmark--ink { color: var(--ink); }
  .wordmark--cream { color: var(--cream); }

  .product-title { font-family: var(--display); font-weight: 800; font-stretch: 125%; text-transform: uppercase; font-size: 36px; line-height: 41px; text-align: center; letter-spacing: 0.01em; white-space: nowrap; }
  .tagline { text-transform: uppercase; font-size: 17px; line-height: 21px; text-align: center; letter-spacing: 0.02em; white-space: nowrap; }
  .ingredients { text-transform: uppercase; font-size: 11px; line-height: 14px; text-align: center; letter-spacing: 0.02em; white-space: nowrap; }
  .size { font-size: 11px; text-align: center; }

  .center { position: absolute; left: 0; right: 0; }

  .lid-sticker { position: absolute; left: 877px; top: 197px; width: 240px; height: 240px; border-radius: 50%; background: var(--cream); display: flex; align-items: center; justify-content: center; }
  .lid-sticker__ring { position: absolute; left: 18px; top: 18px; width: 204px; height: 204px; border-radius: 50%; border: 1.5px solid var(--ink); }
  .lid-sticker .wordmark { font-size: 17px; }

  .outer-box { position: absolute; top: 635px; width: 488px; height: 425px; }
  .outer-box--salve { left: 83px; background: var(--cream); color: var(--ink); }
  .outer-box--lotion { left: 619px; background: var(--ink); color: var(--cream); }
  .outer-box__frame { position: absolute; left: 37px; top: 33px; width: 414px; height: 359px; border: 1.5px solid currentColor; }
</style>
</head>
<body>

  <section class="jar-label" aria-label="Visage Suet Lotion jar label">
    <div class="jar-label__tab">
      <div class="jar-label__brand-tab"><span class="wordmark wordmark--ink">Vale Hollow</span></div>
      <h1 class="product-title center" style="top:86px;color:var(--cream);">Visage Suet<br>Lotion</h1>
    </div>
    <p class="tagline center" style="top:208px;">The strength of tallow,<br>refined for your face</p>
    <p class="ingredients center" style="top:272px;">Grass-fed beef tallow<br>beeswax, honey, vitamin E</p>
    <div class="jar-label__size">60 ml / 2fl. oz.</div>
  </section>

  <section class="lid-sticker" aria-label="Lid sticker">
    <div class="lid-sticker__ring"></div>
    <span class="wordmark wordmark--ink">Vale Hollow</span>
  </section>

  <section class="outer-box outer-box--salve" aria-label="Everyday Suet Salve outer box">
    <div class="outer-box__frame"></div>
    <p class="wordmark wordmark--ink center" style="top:74px;text-align:center;">Vale Hollow</p>
    <h2 class="product-title center" style="top:133px;">Everyday<br>Suet Salve</h2>
    <p class="tagline center" style="top:248px;">Crafted from nature’s<br>simplest elements</p>
    <p class="ingredients center" style="top:305px;">Grass-fed beef tallow<br>beeswax, honey, vitamin E</p>
    <p class="size center" style="top:351px;">60 ml / 2fl. oz.</p>
  </section>

  <section class="outer-box outer-box--lotion" aria-label="Visage Suet Lotion outer box">
    <div class="outer-box__frame"></div>
    <p class="wordmark wordmark--cream center" style="top:74px;text-align:center;">Vale Hollow</p>
    <h2 class="product-title center" style="top:133px;">Visage Suet<br>Lotion</h2>
    <p class="tagline center" style="top:248px;">The strength of tallow,<br>refined for your face</p>
    <p class="ingredients center" style="top:305px;">Grass-fed beef tallow<br>beeswax, honey, vitamin E</p>
    <p class="size center" style="top:351px;">60 ml / 2fl. oz.</p>
  </section>

</body>
</html>
```